Meridale Dental Business Card

Please design a professional but colorful looking business card. Our new logo is attached. The card also needs the following information:
For ALL Your Dental Needs
Curtis L. Hobbel, D.D.S.
555-555-0147
20463-C North Fernwick, Corvale, WX 74031
www.meridaledental.example

Industry/Entity Type

Business

Colors

Designer to choose colors to be used in the design.

```html
<!DOCTYPE html>
<html lang="en">
<head>
<meta charset="utf-8">
<title>Meridale Dental Business Card</title>
<link href="https://fonts.googleapis.com/css2?family=Open+Sans:wght@400;600;700&display=swap" rel="stylesheet">
<style>
  :root {
    --bg: #e9e6e1;
    --green: #6cc04a;
    --green-light: #8fd36b;
    --blue: #2f5fb3;
    --blue-deep: #1f4596;
    --blue-soft: #8fa3dc;
    --red: #ee4b2b;
    --red-light: #f56a3f;
    --navy: #2a3146;
    --white: #ffffff;
  }
  * { margin: 0; padding: 0; box-sizing: border-box; }
  html, body { width: 1200px; height: 899px; overflow: hidden; }
  body {
    background: var(--bg);
    font-family: "Open Sans", Arial, sans-serif;
    position: relative;
  }
  .card {
    position: absolute;
    left: 250px;
    width: 700px;
    height: 400px;
    overflow: hidden;
    box-shadow: 0 6px 18px rgba(0,0,0,.18);
  }
  .card-front { top: 33px; }
  .card-back { top: 466px; background: var(--white); }

  /* front */
  .name-band {
    position: absolute; left: 0; top: 0; width: 100%; height: 92px;
    background: linear-gradient(180deg, var(--green-light), var(--green));
    display: flex; align-items: center; padding-left: 250px;
  }
  .doctor-name { color: var(--white); font-size: 34px; font-weight: 600; letter-spacing: .5px; }
  .info-band {
    position: absolute; left: 0; top: 92px; width: 100%; height: 214px;
    background: linear-gradient(180deg, var(--blue), var(--blue-deep));
  }
  .brand {
    position: absolute; left: 28px; top: 80px;
    display: flex; align-items: center; gap: 10px;
  }
  .brand-square { width: 26px; height: 26px; background: var(--white); }
  .brand-name { color: var(--white); font-size: 24px; font-weight: 700; }
  .contact {
    position: absolute; left: 300px; top: 22px; color: var(--white);
  }
  .phone { font-size: 42px; font-weight: 400; letter-spacing: 2px; margin-bottom: 14px; }
  .address, .web { font-size: 19px; line-height: 1.6; }
  .tagline-band {
    position: absolute; left: 0; top: 306px; width: 100%; height: 94px;
    background: linear-gradient(180deg, var(--red-light), var(--red));
    display: flex; align-items: center; justify-content: center;
  }
  .tagline { color: var(--white); font-size: 36px; font-weight: 400; letter-spacing: 1px; }

  /* back */
  .back-top {
    position: absolute; left: 0; top: 0; width: 100%; height: 110px;
    background: linear-gradient(180deg, var(--blue-soft), rgba(255,255,255,0));
  }
  .back-bottom {
    position: absolute; left: 0; bottom: 0; width: 100%; height: 120px;
    background: linear-gradient(0deg, var(--blue-soft), rgba(255,255,255,0));
  }
  .back-brand {
    position: absolute; left: 0; top: 0; width: 100%; height: 100%;
    display: flex; align-items: center; justify-content: center; gap: 14px;
  }
  .back-brand .brand-square { width: 40px; height: 40px; background: var(--blue); }
  .back-brand .brand-name { color: var(--navy); font-size: 46px; font-weight: 700; }
</style>
</head>
<body>
  <section class="card card-front">
    <div class="name-band"><span class="doctor-name">Curtis L. Hobbel, D.D.S.</span></div>
    <div class="info-band">
      <div class="brand">
        <span class="brand-square"></span>
        <span class="brand-name">Meridale Dental</span>
      </div>
      <div class="contact">
        <p class="phone">555-555-0147</p>
        <p class="address">20463-C North Fernwick, Corvale, WX 74031</p>
        <p class="web">www.meridaledental.example</p>
      </div>
    </div>
    <div class="tagline-band"><span class="tagline">For ALL Your Dental Needs</span></div>
  </section>

  <section class="card card-back">
    <div class="back-top"></div>
    <div class="back-bottom"></div>
    <div class="back-brand">
      <span class="brand-square"></span>
      <span class="brand-name">Meridale Dental</span>
    </div>
  </section>
</body>
</html>
```